We are needing a ONE PAGE FLYER design for our 5th Annual Youth Hunt 2021. This Youth Hunt is a Non-Profit Organization where 'Bright Trail Outings' teams up with 'Dobson Pinegrove Ranch' & 'Stone Brook Pastures' and they bring these amazing kids to come out to a high fenced ranch(s) to learn how to hunt and harvest their own deer. These kids then get to take ALL the meat that was harvested back home where they help feed their families for the rest of the year. Not only do they learn to live off the land, but this organization teaches them all the life skills that they don't have the ability to learn at home in the city. This program gets inner city kids outdoors and helps promote a life long work ethic attitude. These kids grow up to become Valedictorian of their classes and receive scholarships to some of the best colleges around the nation.
I have attached the Bright Trail Outings (who is the main organization) logo as well as Dobson Pinegrove Ranch & Stone Brook Pastures logo (The Thornburys on the previous years flyer). Also attached you will find the past couple of years flyer that we have been using...yes I said couple of years... we are needing a revamp :) We will need to incorporate all 3 logos on the flyer along with the saying "5th Annual Youth Hunt 2021".

```html
<!DOCTYPE html>
<html lang="en">
<head>
<meta charset="utf-8">
<title>5th Annual Youth Hunt 2021</title>
<link href="https://fonts.googleapis.com/css2?family=Bebas+Neue&family=Lato:wght@400;700&family=Oswald:wght@600&display=swap" rel="stylesheet">
<style>
  :root {
    --page-bg: #a3a3a3;
    --ink: #050505;
    --paper: #ffffff;
    --soft: #e9e9e9;
    --mist-dark: #1a1a1a;
    --mist-mid: #5a5a5a;
    --mist-light: #8a8a8a;
  }
  * { margin: 0; padding: 0; box-sizing: border-box; }
  html, body { width: 1200px; height: 1200px; overflow: hidden; }
  body {
    background: var(--page-bg);
    font-family: "Lato", sans-serif;
    color: var(--paper);
    position: relative;
  }
  .flyer {
    position: absolute;
    left: 140px; top: 8px;
    width: 920px; height: 1184px;
    background: var(--ink);
    overflow: hidden;
  }
  .field-photo {
    position: absolute;
    left: 0; right: 0; top: 560px; bottom: 0;
    background: linear-gradient(180deg, var(--ink) 0%, var(--mist-dark) 14%, #3a3a3a 32%, var(--mist-mid) 52%, var(--mist-light) 64%, var(--mist-mid) 76%, #2e2e2e 100%);
  }
  .sponsor-row {
    position: absolute; top: 50px; left: 0; right: 0; height: 110px;
    display: flex; justify-content: space-around; align-items: center;
    padding: 0 30px;
  }
  .sponsor {
    display: flex; align-items: center; gap: 10px;
    font-family: "Lato", sans-serif; font-weight: 700; font-size: 22px;
    text-transform: uppercase; letter-spacing: 1px; line-height: 1.1;
    color: var(--paper); text-align: center;
  }
  .sponsor .dot {
    width: 16px; height: 16px; border-radius: 50%; background: var(--paper); flex: none;
  }
  .presenters {
    position: absolute; top: 218px; width: 100%;
    text-align: center; font-size: 14px;
  }
  .title {
    position: absolute; top: 242px; width: 100%;
    text-align: center;
    font-family: "Bebas Neue", sans-serif; font-size: 88px; line-height: 1;
    letter-spacing: 1px;
  }
  .tagline {
    position: absolute; top: 333px; left: 0; right: 0; height: 74px;
    background: var(--paper); color: var(--ink);
    display: flex; align-items: center; justify-content: center;
    text-align: center; font-weight: 700; font-size: 24px; line-height: 31px;
  }
  .intro {
    position: absolute; top: 437px; left: 40px; right: 40px;
    text-align: center; font-size: 16px; line-height: 21px;
  }
  .rule {
    position: absolute; left: 185px; width: 550px; height: 2px;
    background: linear-gradient(90deg, transparent, var(--soft) 15%, var(--soft) 85%, transparent);
  }
  .rule.top { top: 589px; }
  .rule.bottom { top: 670px; }
  .appeal {
    position: absolute; top: 606px; width: 100%;
    text-align: center; font-size: 19px; line-height: 25px; text-transform: uppercase;
  }
  .donation-label {
    position: absolute; top: 706px; left: 359px; width: 185px; height: 32px;
    border-radius: 16px; background: var(--paper); color: var(--ink);
    display: flex; align-items: center; justify-content: center; font-size: 19px;
    text-transform: uppercase;
  }
  .donation-list {
    position: absolute; top: 753px; left: 70px; right: 70px;
    text-align: center; font-size: 19px; line-height: 24.5px;
  }
  .send-to {
    position: absolute; top: 952px; left: 97px; font-size: 15px;
  }
  .address {
    position: absolute; top: 978px; left: 97px;
    display: flex; gap: 12px; align-items: flex-start;
  }
  .address svg { width: 28px; height: 36px; margin-top: 2px; }
  .address p { font-size: 15px; line-height: 19.5px; text-transform: uppercase; }
  .closing {
    position: absolute; top: 1080px; width: 100%;
    text-align: center; font-family: "Oswald", sans-serif; font-weight: 600;
    font-size: 46px; text-transform: uppercase; letter-spacing: 0.5px;
  }
</style>
</head>
<body>
  <main class="flyer">
    <div class="field-photo" role="img" aria-label="Misty black and white meadow at dawn with a stag standing in tall grass"></div>

    <header class="sponsor-row">
      <div class="sponsor"><span class="dot"></span>Dobson Pinegrove<br>Ranch</div>
      <div class="sponsor">Bright Trail<br>Outings</div>
      <div class="sponsor">Stone Brook<br>Pastures</div>
    </header>

    <p class="presenters">Dobson Pinegrove Ranch, The Thornbury's, &amp; Bright Trail Outings Proudly Present...</p>
    <h1 class="title">5th Annual Youth Hunt 2021</h1>

    <div class="tagline"><p>The Youth are the future of our nation, together we can help them<br>learn to appreciate the outdoors!</p></div>

    <p class="intro">Dobson Pinegrove Ranch, the Thornbury's, &amp; Bright Trail Outings will be sponsoring THE 5th Annual Youth Hunt<br>on october , 2021 at Dobson Pinegrove Ranch.We are lookiong forward to being able to provide both an<br>educational &amp; fun experiencefor all children. Over the weekend, we will educate our youth on the mechanics<br>&amp; SPORT OF HUNTING. ThisYear's event will host boys &amp; girls aged 6-14 at the Dobson Pinegrove Ranch.<br>In order to makethis event happen we are looking donations<br>to help support these deserving youth.</p>

    <div class="rule top"></div>
    <p class="appeal">Anyone interested in helping our cause can<br>donate goods or support monetarily.</p>
    <div class="rule bottom"></div>

    <div class="donation-label">Donation List</div>
    <p class="donation-list">Trailmart Gift Cads - Cases of bottled water - slightly used hunting gear - Sportade Powder<br>Mix Porchlight Lemonade Powder Mix - Paper Plates - Paper Towels- Plastic<br>Utensils - Plastic Keepwell<br>Aluminium foil - Sealtite Bags - Non-Perishable Individually Wrapped Snacks<br>Granola Bars<br>PROTEIN BARS - .223/.243 SHELLS</p>

    <p class="send-to">Please Send Donations To</p>
    <div class="address">
      <svg viewBox="0 0 28 36" aria-hidden="true"><path d="M14 1C7 1 1.5 6.5 1.5 13.2 1.5 22 14 35 14 35s12.5-13 12.5-21.8C26.5 6.5 21 1 14 1z" fill="#fff"/><circle cx="14" cy="13" r="5" fill="#555"/></svg>
      <p>Dobson Holdings LP<br>482 Cedar Bend Road<br>Marlow Springs, TX. 75120</p>
    </div>

    <p class="closing">We greatly appreciate your generosity !</p>
  </main>
</body>
</html>
```